shopfitters cards and stationery
Stationery
Project: shopfitters cards and stationery
shopfitters cards and stationery  - Construction
Creative Brief
Professional
Mark Pelling
Contracts Manager
7/24 Quarry Lane Wendale 4182
mark@fitwrightgroup.com.au
www.fitwrightgroup.com.au
Phone numbers and other details etc will change if you could use them for know that will be great. give me your best work :) Thanks

```html
<!DOCTYPE html>
<html lang="en">
<head>
<meta charset="utf-8">
<title>Fitwright Group – Business Card</title>
<link rel="stylesheet" href="https://fonts.googleapis.com/css2?family=Michroma&display=swap">
<style>
  :root {
    --stage: #e9eaec;
    --card-white: #ffffff;
    --brand-blue: #1f2f8f;
    --brand-blue-deep: #17237a;
    --brand-blue-light: #2f45b5;
    --swoosh-grey: #8a8d94;
    --swoosh-light: #d4d6da;
    --text-slate: #5a6a9a;
    --text-white: #ffffff;
  }
  * { margin: 0; padding: 0; box-sizing: border-box; }
  html, body {
    width: 1200px; height: 823px; overflow: hidden;
    background: var(--stage);
    font-family: "Michroma", sans-serif;
  }
  .card {
    position: absolute; left: 150px; top: 151px;
    width: 900px; height: 520px;
    border-radius: 36px; overflow: hidden;
    background: var(--card-white);
    box-shadow: 0 10px 30px rgba(0,0,0,0.18);
  }
  .card-art { position: absolute; inset: 0; }
  .brand {
    position: absolute; top: 120px; left: 0; right: 0;
    display: flex; align-items: center; justify-content: center; gap: 22px;
  }
  .brand-dot {
    width: 78px; height: 78px; border-radius: 50%;
    background: var(--brand-blue);
  }
  .brand-name {
    color: var(--brand-blue);
    font-size: 40px; line-height: 1.1; letter-spacing: 2px;
    text-transform: uppercase;
  }
  .person {
    position: absolute; top: 306px; left: 410px;
    display: flex; align-items: center; gap: 16px;
    color: var(--text-slate); font-size: 15px; letter-spacing: 1px;
    text-transform: uppercase;
  }
  .person-divider { width: 1px; height: 22px; background: var(--text-slate); }
  .contact {
    position: absolute; left: 48px; right: 40px; bottom: 30px;
    color: var(--text-white); font-size: 11.5px; letter-spacing: 0.6px;
    text-transform: uppercase;
  }
  .contact-row { display: flex; gap: 18px; align-items: center; margin-top: 10px; }
  .contact-item { display: flex; align-items: center; gap: 7px; white-space: nowrap; }
  .contact-item svg { width: 14px; height: 14px; flex: none; }
</style>
</head>
<body>
  <div class="card">
    <svg class="card-art" viewBox="0 0 900 520" width="900" height="520" aria-hidden="true">
      <defs>
        <linearGradient id="swoosh" x1="0" y1="0" x2="1" y2="0">
          <stop offset="0" stop-color="#ffffff"/>
          <stop offset="0.35" stop-color="#d4d6da"/>
          <stop offset="1" stop-color="#8a8d94"/>
        </linearGradient>
        <linearGradient id="band" x1="0" y1="0" x2="0" y2="1">
          <stop offset="0" stop-color="#2f45b5"/>
          <stop offset="1" stop-color="#17237a"/>
        </linearGradient>
      </defs>
      <path d="M0,392 Q420,372 900,318 L900,345 Q420,392 0,410 Z" fill="url(#swoosh)"/>
      <path d="M0,410 Q420,392 900,345 L900,520 L0,520 Z" fill="url(#band)"/>
    </svg>

    <div class="brand">
      <span class="brand-dot"></span>
      <span class="brand-name">Fitwright<br>Group</span>
    </div>

    <div class="person">
      <span class="person-name">Mark Pelling</span>
      <span class="person-divider"></span>
      <span class="person-role">Contracts Manager</span>
    </div>

    <div class="contact">
      <div class="contact-row">
        <span class="contact-item">
          <svg viewBox="0 0 14 14"><circle cx="7" cy="7" r="7" fill="#fff"/><path d="M7 3.2a2.4 2.4 0 0 0-2.4 2.4C4.6 7.5 7 10.8 7 10.8s2.4-3.3 2.4-5.2A2.4 2.4 0 0 0 7 3.2z" fill="#1f2f8f"/></svg>
          7/24 Quarry Lane Wendale 4182
        </span>
        <span class="contact-item">
          <svg viewBox="0 0 14 14"><circle cx="7" cy="7" r="7" fill="#fff"/><path d="M4.5 3.5l1.4-.3.8 2-1 .7a5 5 0 0 0 2.4 2.4l.7-1 2 .8-.3 1.4c-3.3.3-6.3-2.7-6-6z" fill="#1f2f8f"/></svg>
          07 5550 1284
        </span>
        <span class="contact-item">
          <svg viewBox="0 0 14 14"><circle cx="7" cy="7" r="7" fill="#fff"/><rect x="5" y="3" width="4" height="8" rx="0.8" fill="#1f2f8f"/></svg>
          0400 555 217
        </span>
      </div>
      <div class="contact-row">
        <span class="contact-item">
          <svg viewBox="0 0 14 14"><circle cx="7" cy="7" r="7" fill="#fff"/><rect x="3.5" y="4.5" width="7" height="5" fill="#1f2f8f"/></svg>
          07 5550 3396
        </span>
        <span class="contact-item">
          <svg viewBox="0 0 14 14"><circle cx="7" cy="7" r="7" fill="#fff"/><path d="M3.5 4.5h7v5h-7z M3.5 4.5l3.5 2.7 3.5-2.7" fill="none" stroke="#1f2f8f" stroke-width="1"/></svg>
          mark@fitwrightgroup.com.au
        </span>
        <span class="contact-item">
          <svg viewBox="0 0 14 14"><circle cx="7" cy="7" r="7" fill="#fff"/><circle cx="7" cy="7" r="3.5" fill="none" stroke="#1f2f8f" stroke-width="1"/><path d="M3.5 7h7" stroke="#1f2f8f" stroke-width="1"/></svg>
          www.fitwrightgroup.com.au
        </span>
      </div>
    </div>
  </div>
</body>
</html>
```